Learn-to-Swim Program for Children's Day Camp (Walter Brightley Fieldgrounds)

We are a children's camp with a robust swim instruction program and we need a series of 5 kid-friendly banners which list the skills learned in our swim program that can be hung up around each outdoor pool complex. All together there are 6 overarching levels and 12 sublevels (see attached). Except for the Level V & VI, each banner should be one overarching level and the 2-3 sublevels that define it.

Each swim level has a name, most of which are sea creatures, and we want to have a corresponding image/avatar to go with the swim level name (e.g. tadpole, barracuda, orca, goldfish, catfish).

The banners should be 3 feet (width) by 5 feet (height). The banners will be hung outdoors so it needs a color scheme that won't get lost in the sunlight.

We will want to include our logo but do not need the design to match our logo colors. Logo can be in black or white.

Our website is: www.campwbf.example

Target Market(s)

children age 5 - 12

Industry/Entity Type

children's day camp

Requirements
Must have
• A progression from level I to level VI. Should have a happy, bright, fun, tone, text MUST be legible from at least a 5 foot distance
Should not have
• adult themes, a scheme that evokes sadness or fear

```html
<!DOCTYPE html>
<html lang="en">
<head>
<meta charset="utf-8">
<title>Walter Brightley Fieldgrounds – Wader &amp; Splasher Arc I</title>
<link rel="stylesheet" href="https://fonts.googleapis.com/css2?family=Fredoka:wght@500&family=Quicksand:wght@500;600&display=swap">
<style>
  :root {
    --backdrop: #e6e6e6;
    --sky-top: #b6c9ec;
    --paper: #ffffff;
    --ink: #111111;
    --title-blue: #8eaee6;
    --title-green: #9ccf86;
    --tag-blue: #8aa6d8;
    --tag-green: #a6d98f;
    --water-light: #d7effb;
    --water-mid: #7cc8ee;
    --water-deep: #3a9fd9;
  }
  * { box-sizing: border-box; margin: 0; padding: 0; }
  html, body { width: 1200px; height: 1200px; overflow: hidden; }
  body { background: var(--backdrop); position: relative; font-family: "Quicksand", sans-serif; color: var(--ink); }

  .banner {
    position: absolute; left: 285px; top: 71px; width: 631px; height: 1055px;
    background: linear-gradient(to bottom, var(--sky-top) 0, var(--paper) 250px, var(--paper) 100%);
    overflow: hidden;
  }
  .brand {
    position: absolute; top: 72px; left: 0; width: 100%;
    display: flex; justify-content: center; align-items: center; gap: 10px;
    font-weight: 600; font-size: 20px; letter-spacing: 0.5px; color: var(--ink);
  }
  .brand-square { width: 22px; height: 22px; background: var(--ink); }

  .level-title {
    position: absolute; left: 0; width: 100%; text-align: center;
    font-family: "Fredoka", sans-serif; font-weight: 500; font-size: 60px; letter-spacing: 3px;
    color: var(--paper); -webkit-text-stroke: 2.5px var(--title-blue); line-height: 1;
  }
  .level-title .arc { -webkit-text-stroke-color: var(--title-green); }
  .title-wader { top: 180px; }
  .title-splasher { top: 487px; }

  .skills-tag { position: absolute; left: 0; width: 150px; height: 125px; }
  .tag-wader { top: 242px; }
  .tag-splasher { top: 562px; }

  .skill-list {
    position: absolute; left: 173px; list-style: none;
    font-size: 15.5px; font-weight: 500; line-height: 20.5px;
  }
  .skill-list li::before { content: "> "; }
  .skills-wader { top: 255px; }
  .skills-splasher { top: 564px; }

  .move-up {
    position: absolute; font-size: 35px; font-weight: 500; line-height: 1;
  }
  .move-up-wader { top: 370px; left: 0; width: 100%; text-align: center; }
  .requirement-wader {
    position: absolute; top: 416px; left: 0; width: 100%; text-align: center;
    font-size: 21px; font-weight: 500;
  }

  .pool-scene {
    position: absolute; left: 0; top: 680px; width: 100%; height: 375px;
    background: linear-gradient(to bottom, var(--water-light) 0, var(--water-mid) 22%, var(--water-deep) 100%);
  }
  .pool-scene svg { position: absolute; left: 0; top: -22px; }

  .move-up-splasher { top: 692px; right: 36px; text-align: right; }
  .requirement-splasher {
    position: absolute; top: 738px; right: 38px; width: 320px; text-align: center;
    font-size: 21.5px; font-weight: 500; line-height: 30px;
  }
  .site-url {
    position: absolute; left: 37px; top: 988px;
    font-size: 20px; font-weight: 600; letter-spacing: 5px;
  }
</style>
</head>
<body>
  <main class="banner">
    <div class="brand"><span class="brand-square"></span>Walter Brightley Fieldgrounds</div>

    <h1 class="level-title title-wader">WADER <span class="arc">ARC I</span></h1>

    <svg class="skills-tag tag-wader" viewBox="0 0 150 125" aria-hidden="true">
      <defs>
        <linearGradient id="tagFill" x1="0" y1="0" x2="1" y2="1">
          <stop offset="0" stop-color="var(--tag-blue)"/>
          <stop offset="1" stop-color="var(--tag-green)"/>
        </linearGradient>
      </defs>
      <path d="M0 95 L120 28 Q140 14 142 26 Q132 40 120 48 L0 122 Z" fill="url(#tagFill)"/>
      <text x="62" y="84" transform="rotate(-30 62 84)" font-family="Quicksand, sans-serif" font-size="16" font-weight="600" fill="#111" text-anchor="middle">SKILLS</text>
    </svg>

    <ul class="skill-list skills-wader">
      <li>Gets into the water with assistance</li>
      <li>Follows pool rules</li>
      <li>Can hold big breath and get chin/ cheeks in water</li>
      <li>Cups hands to hold water and get some of face wet</li>
      <li>Doesn't always need assistance in water</li>
    </ul>

    <h2 class="move-up move-up-wader">Move-Up</h2>
    <p class="requirement-wader">Must be comfortable entering the water</p>

    <h1 class="level-title title-splasher">SPLASHER <span class="arc">ARC I</span></h1>

    <svg class="skills-tag tag-splasher" viewBox="0 0 150 125" aria-hidden="true">
      <path d="M0 95 L120 28 Q140 14 142 26 Q132 40 120 48 L0 122 Z" fill="url(#tagFill)"/>
      <text x="62" y="84" transform="rotate(-30 62 84)" font-family="Quicksand, sans-serif" font-size="16" font-weight="600" fill="#111" text-anchor="middle">SKILLS</text>
    </svg>

    <ul class="skill-list skills-splasher">
      <li>Enters and exits pool without assistance</li>
      <li>Can do a slide in entry</li>
      <li>Plays in water up to chest deep</li>
      <li>Dips face and head in water</li>
      <li>Blows bubbles through the mouth</li>
    </ul>

    <div class="pool-scene" role="img" aria-label="Illustration of two cartoon children floating on striped swim rings in a bright blue pool with white splashing waves">
      <svg width="631" height="60" viewBox="0 0 631 60" aria-hidden="true">
        <path d="M0 30 Q80 5 160 26 T330 22 T500 28 T631 18 L631 60 L0 60 Z" fill="var(--water-light)"/>
      </svg>
    </div>

    <h2 class="move-up move-up-splasher">Move-Up</h2>
    <p class="requirement-splasher">Must fully submerge body and head underwater (no nose holding)</p>

    <p class="site-url">www.campwbf.example</p>
  </main>
</body>
</html>
```